HOME IMPROVEMENT Business Card

I want a very unique business card. nothing typical and boring. Im open to you ideas. Ive seen cards with gold and silver or color foil and spot UV coatings. Im looking for something that looks cool and grabs attention. I like rounded corners but am open to all suggestions. We are a home improvement company and I will have a presentation folder printed and a catalog printed also and want to keep that same theme. I love the colors in our logo but I am open at looking at a 3rd color that would work with my logo. I hope that helps.
Card should include
Address
Phone
Fax
Email
Website
Target Market(s)
Home owners, people looking to remodel their home
Industry/Entity Type
Home Improvement
Contact Information for Business Card
2873 Maple Crest Avenue Unit 410
Des Plaines, Il 60284
Phone
Direct Line
Email
Website
Font styles to use
Other font styles liked:
- IM OPEN MINDED
Requirements
Must have
- High end quality look nothing boring I like rounded corners but am open minded
Nice to have
- WOW. I want something nice and impressive.
Should not have
- ??? Not sure

```html
<!DOCTYPE html>
<html lang="en">
<head>
<meta charset="utf-8">
<title>Keystead Business Card</title>
<link href="https://fonts.googleapis.com/css2?family=Saira+Semi+Condensed:wght@600;700&family=Ubuntu:wght@400&display=swap" rel="stylesheet">
<style>
  :root {
    --backdrop: #6e6e6e;
    --navy: #0b1038;
    --green: #0b8a3b;
    --paper: #ffffff;
    --ink: #161a45;
  }
  * { margin: 0; padding: 0; box-sizing: border-box; }
  html, body { width: 1200px; height: 900px; overflow: hidden; }
  body { background: var(--backdrop); position: relative; font-family: "Ubuntu", sans-serif; }

  .card { position: absolute; top: 271px; width: 458px; height: 283px; overflow: hidden; }
  .card-front { left: 137px; background: var(--paper); }
  .card-back { left: 626px; background: var(--navy); height: 281px; }

  .brand-name {
    position: absolute; font-family: "Saira Semi Condensed", sans-serif; font-weight: 700;
    white-space: nowrap; display: flex; align-items: center; gap: 10px;
  }
  .brand-mark { display: inline-block; width: 14px; height: 14px; }
  .card-front .brand-name { left: 28px; top: 117px; font-size: 40px; color: var(--navy); }
  .card-front .brand-mark { background: var(--green); }
  .card-back .brand-name { left: 0; right: 0; justify-content: center; top: 112px; font-size: 52px; color: var(--paper); }
  .card-back .brand-mark { background: var(--green); width: 16px; height: 16px; }

  .contact { position: absolute; left: 252px; top: 51px; color: var(--ink); }
  .contact-name { font-family: "Saira Semi Condensed", sans-serif; font-weight: 700; font-size: 21px; letter-spacing: 0.5px; color: var(--green); line-height: 24px; }
  .contact-title { font-size: 11.5px; letter-spacing: 0.3px; line-height: 14px; }
  .contact-lines { list-style: none; margin-top: 17px; font-size: 13px; line-height: 19px; }
  .contact-lines li { display: flex; align-items: center; gap: 5px; }
  .contact-lines svg { width: 11px; height: 11px; fill: var(--green); flex: none; }
  .contact-address { margin-top: 15px; font-size: 12.5px; line-height: 17px; font-style: normal; }

  .band { position: absolute; left: 0; bottom: 0; width: 458px; height: 30px; }
  .strip { position: absolute; left: 0; width: 100%; height: 11px; background: var(--green); }
  .strip-top { top: 0; }
  .strip-bottom { bottom: 0; }
</style>
</head>
<body>

<section class="card card-front">
  <div class="brand-name"><span class="brand-mark"></span>Keystead</div>

  <div class="contact">
    <h1 class="contact-name">DANIEL MERCER</h1>
    <p class="contact-title">DIRECTOR</p>
    <ul class="contact-lines">
      <li><svg viewBox="0 0 12 12"><path d="M1 4c0-2 2-3 5-3s5 1 5 3l-2 1-1-1.5H4L3 5 1 4zm2 2h6l1 5H2l1-5zm3 1a1.5 1.5 0 100 3 1.5 1.5 0 000-3z"/></svg>712-5550-148 (Direct)</li>
      <li><svg viewBox="0 0 12 12"><path d="M1 4c0-2 2-3 5-3s5 1 5 3l-2 1-1-1.5H4L3 5 1 4zm2 2h6l1 5H2l1-5zm3 1a1.5 1.5 0 100 3 1.5 1.5 0 000-3z"/></svg>717-(555)-026</li>
      <li><svg viewBox="0 0 12 12"><path d="M1 2.5h10v7H1zM1.6 3l4.4 3.4L10.4 3" stroke="#fff" stroke-width="0.8"/></svg>info@keysteadgroup.com</li>
      <li><svg viewBox="0 0 12 12"><circle cx="6" cy="6" r="5"/><path d="M3 4l2 1 0 2 2 1 1 2M7 2l1 2 2 0" stroke="#fff" stroke-width="0.8" fill="none"/></svg>www.keysteadgroup.com</li>
    </ul>
    <address class="contact-address">2873 Maple Crest Avenue Unit 410<br>Des Plaines, Il 60284</address>
  </div>

  <svg class="band" viewBox="0 0 458 30" aria-hidden="true">
    <polygon points="0,13 220,15 212,30 0,30" fill="var(--green)"/>
    <polygon points="238,2 458,2 458,30 220,30" fill="var(--navy)"/>
  </svg>
</section>

<section class="card card-back">
  <div class="strip strip-top"></div>
  <div class="brand-name"><span class="brand-mark"></span>Keystead</div>
  <div class="strip strip-bottom"></div>
</section>

</body>
</html>
```